Design for Certificate

Design a certificate for training, providing our company logo such as attachments. Company's name is "ØSTRA Velmark Advisory Ltd", please refer to our company profile: https://www.ostra-velmark.example/company_info

The style of the current certificate is also attached, and another certificate of another company can be referred to. Psd & jpg are required for the final draft (the layers of psd are not merged). Thanks!

```html
<!DOCTYPE html>
<html lang="en">
<head>
<meta charset="utf-8">
<title>ØSTRA Velmark – Certificate of Completion</title>
<link rel="stylesheet" href="https://fonts.googleapis.com/css2?family=Alegreya:ital,wght@0,700;1,400;1,500;1,700&display=swap">
<style>
  :root {
    --paper: #fbf8f1;
    --paper-edge: #f3ebdc;
    --ink: #3a3b3d;
    --gold: #c09a5b;
    --gold-faint: #efe4d2;
    --navy: #2b2a8e;
    --ornament-ink: rgba(58, 59, 61, 0.22);
    --ornament-gold: rgba(192, 154, 91, 0.35);
  }
  html, body {
    margin: 0;
    padding: 0;
    overflow: hidden;
    background: var(--paper);
  }
  .certificate {
    display: block;
    width: 849px;
    height: 1200px;
  }
  .brand-name { font-family: "Alegreya", serif; font-weight: 700; fill: var(--ink); }
  .title-main { font-family: "Alegreya", serif; font-style: italic; font-weight: 500; fill: var(--ink); }
  .title-sub { font-family: "Alegreya", serif; font-style: italic; font-weight: 500; fill: var(--gold); }
  .body-line { font-family: "Alegreya", serif; font-style: italic; font-weight: 400; fill: var(--ink); }
  .course-name { font-family: "Alegreya", serif; font-style: italic; font-weight: 700; fill: var(--navy); }
  .course-type { font-family: "Alegreya", serif; font-style: italic; font-weight: 700; fill: var(--ink); }
  .issuer { font-family: "Alegreya", serif; font-weight: 700; fill: var(--ink); }
  .rule-ink { stroke: var(--ink); stroke-width: 1; }
  .rule-gold { stroke: var(--gold); stroke-width: 1.5; }
  .frame { fill: none; stroke: var(--ink); stroke-width: 4; }
  .inner-frame { fill: none; stroke: var(--gold-faint); stroke-width: 7; }
  .corner-ornament { fill: var(--ornament-ink); }
  .flourish { fill: var(--ornament-gold); }
</style>
</head>
<body>
<svg class="certificate" viewBox="0 0 849 1200" xmlns="http://www.w3.org/2000/svg">
  <defs>
    <radialGradient id="paper-glow" cx="50%" cy="50%" r="70%">
      <stop offset="0%" stop-color="#ffffff"/>
      <stop offset="100%" stop-color="#f3ebdc"/>
    </radialGradient>
  </defs>

  <!-- Paper -->
  <rect class="paper" x="0" y="0" width="849" height="1200" fill="url(#paper-glow)"/>

  <!-- Faint inner frames -->
  <rect class="inner-frame" x="198" y="154" width="462" height="892"/>
  <rect class="inner-frame" x="157" y="192" width="544" height="817"/>

  <!-- Outer frame -->
  <g class="outer-frame">
    <line class="frame" x1="97" y1="33" x2="752" y2="33"/>
    <line class="frame" x1="97" y1="1171" x2="752" y2="1171"/>
    <line class="frame" x1="40" y1="138" x2="40" y2="1062"/>
    <line class="frame" x1="811" y1="138" x2="811" y2="1062"/>
  </g>

  <!-- Corner ornaments -->
  <rect class="corner-ornament" x="31" y="37" width="92" height="125" role="img" aria-label="Fretwork corner ornament, top left"/>
  <rect class="corner-ornament" x="726" y="37" width="92" height="125" role="img" aria-label="Fretwork corner ornament, top right"/>
  <rect class="corner-ornament" x="31" y="1038" width="92" height="125" role="img" aria-label="Fretwork corner ornament, bottom left"/>
  <rect class="corner-ornament" x="726" y="1038" width="92" height="125" role="img" aria-label="Fretwork corner ornament, bottom right"/>

  <!-- Top and bottom gold rules with flourishes -->
  <line class="rule-gold" x1="133" y1="70" x2="318" y2="70"/>
  <line class="rule-gold" x1="523" y1="70" x2="708" y2="70"/>
  <rect class="flourish" x="330" y="60" width="180" height="21" rx="10" role="img" aria-label="Gold scroll flourish"/>
  <line class="rule-gold" x1="133" y1="1129" x2="318" y2="1129"/>
  <line class="rule-gold" x1="523" y1="1129" x2="708" y2="1129"/>
  <rect class="flourish" x="330" y="1119" width="180" height="21" rx="10" role="img" aria-label="Gold scroll flourish"/>

  <!-- Side flourishes -->
  <rect class="flourish" x="70" y="460" width="32" height="282" rx="14" role="img" aria-label="Vertical gold scroll flourish, left"/>
  <rect class="flourish" x="746" y="460" width="32" height="282" rx="14" role="img" aria-label="Vertical gold scroll flourish, right"/>

  <!-- Brand name -->
  <text class="brand-name" x="424.5" y="212" text-anchor="middle" font-size="64" letter-spacing="3">ØSTRA</text>

  <!-- Title -->
  <text class="title-main" x="424.5" y="340" text-anchor="middle" font-size="116">Certificate</text>
  <text class="title-sub" x="424.5" y="421" text-anchor="middle" font-size="72">of Completion</text>
  <rect class="flourish" x="366" y="466" width="112" height="26" rx="12" role="img" aria-label="Small gold scroll flourish"/>

  <!-- Recipient -->
  <text class="body-line" x="427" y="533" text-anchor="middle" font-size="33">This certificate is awarded to</text>
  <line class="rule-ink" x1="133" y1="629" x2="719" y2="629"/>

  <!-- Course -->
  <text class="body-line" x="427" y="672" text-anchor="middle" font-size="33">has succesfully completed</text>
  <text class="course-name" x="426" y="740" text-anchor="middle" font-size="49">Brand Reputation Management</text>
  <text class="course-type" x="427" y="803" text-anchor="middle" font-size="52">Training Course</text>

  <!-- Details -->
  <text class="body-line" x="206" y="868" font-size="29">Sixteen hours, held on</text>
  <line class="rule-ink" x1="455" y1="870" x2="643" y2="870"/>
  <text class="issuer" x="424.5" y="916" text-anchor="middle" font-size="34">ØSTRA Velmark</text>

  <!-- Signature -->
  <line class="rule-ink" x1="314" y1="1033" x2="536" y2="1033"/>
  <text class="body-line" x="426" y="1059" text-anchor="middle" font-size="19">Chief Technology Officer</text>

  <!-- Certificate number -->
  <text class="body-line" x="146" y="1103" font-size="19">Certificate No.</text>
  <line class="rule-ink" x1="254" y1="1104" x2="413" y2="1104"/>
</svg>
</body>
</html>
```